Lanterns Valley Foundation Web Design

The design we need is for a WordPress blog that will be our content platform. We are a registered 501(c)3 non-profit that focuses on financially supporting the treatment of cancer patients that have been told they have no hope and there is nothing the conventional medical system can do for them. Through this wesbite we want to both rasie awareness about the treatment options plus, raise funds for treating patients. The two primary target audiences of the site are...

1. Terminally ill patients and their families to let them know that there is an option other then hospice and that we are hear to support that option.

2. People looking to help donate to a worthwhile cause that resonates with them.

The website is https://lanternsvalleyfoundation.org/

See attached logo designs!!!

Target Market(s)

Cancer patients and their families

Industry/Entity Type

Foundation

Font styles to use
Sans Serif

Colors
ffffff
fbed22

Requirements
Must have
• I like this look of this site. It is clean, simple, helpful, soft. I like the flow of the pages.
• http://www.brightpathgiving.org/
• I like the design and flow but NOT the color or boldness
• https://tqsn-youth.org/
• I like this style for a donation page.
• https://www.healingscience.org/we-are-hsa/join-the-cause/donations/one-time-donation
• with the addition of a Would you like your employer to match? button.
Nice to have
• White black and gold - but soft
• Even possibly grayscale like the site I like.

```html
<!DOCTYPE html>
<html lang="en">
<head>
<meta charset="utf-8">
<title>Lanterns Valley Foundation</title>
<link rel="stylesheet" href="https://fonts.googleapis.com/css2?family=Crimson+Text:wght@400;600;700&family=Lato:wght@400;700&display=swap">
<style>
:root{
  --gold:#efc552;
  --gold-soft:#f3d57c;
  --ink:#222222;
  --dark:#333333;
  --grey-bg:#efefef;
  --text:#555555;
  --white:#ffffff;
  --sky-top:#2aa9e3;
  --sky-bottom:#1fb2ea;
  --line:#dddddd;
  --art-light:#f4f7f9;
  --art-warm:#f4b183;
}
*{box-sizing:border-box;margin:0;padding:0}
html,body{width:1200px;height:3719px;overflow:hidden}
body{position:relative;background:var(--white);font-family:"Lato",Arial,sans-serif;color:var(--text)}
.abs{position:absolute}
.btn{position:absolute;display:flex;align-items:center;justify-content:center;font-family:"Crimson Text",Georgia,serif;font-size:18px;letter-spacing:1px;text-transform:uppercase;color:var(--ink)}
.btn-gold{background:var(--gold)}
.btn-dark{background:var(--dark);color:var(--white)}

/* header */
.topbar{left:0;top:0;width:1200px;height:112px;background:#f6f6f6}
.brand{left:80px;top:34px;display:flex;align-items:center;gap:12px;font-family:"Crimson Text",Georgia,serif;font-weight:700;font-size:22px;color:var(--ink);letter-spacing:.5px}
.brand-mark{width:28px;height:28px;background:var(--gold)}
.social{display:flex;gap:14px;left:757px;top:36px}
.social span{width:38px;height:38px;border-radius:50%;background:var(--white);border:1px solid var(--line)}
.contact-btn{left:957px;top:35px;width:164px;height:47px}
.nav{left:0;top:112px;width:1200px;height:54px;border-top:1px solid var(--line);border-bottom:1px solid var(--line);background:var(--white)}
.nav a{position:absolute;top:15px;font-size:17px;color:var(--text);text-decoration:none}
.nav a.active{color:var(--ink);border-bottom:3px solid var(--gold);padding-bottom:9px}

/* hero */
.hero{left:0;top:166px;width:1200px;height:541px;background:linear-gradient(180deg,var(--sky-top),var(--sky-bottom))}
.hero-cloud{left:0;top:40px;width:520px;height:150px;background:radial-gradient(ellipse at 40% 50%,rgba(255,255,255,.75),rgba(255,255,255,0) 70%)}
.hero-title{left:79px;top:194px;font-family:"Crimson Text",Georgia,serif;font-weight:400;font-size:40px;line-height:44px;color:#223322}
.hero-art{left:578px;top:69px;width:513px;height:402px;background:linear-gradient(135deg,var(--art-light),var(--art-warm))}

/* welcome */
.frame{left:79px;top:746px;width:412px;height:414px;border:32px solid var(--gold)}
.welcome-photo{left:149px;top:808px;width:416px;height:414px;border:2px solid var(--gold);background:linear-gradient(135deg,#f4f0ee,#e8d9d3 60%,#d6c2bb)}
.welcome-title{left:600px;top:818px;width:500px;font-family:"Crimson Text",Georgia,serif;font-weight:600;font-size:40px;line-height:44px;color:var(--ink)}
.welcome-text{left:600px;top:918px;width:500px;font-size:14px;line-height:24px}
.learn{left:600px;top:998px;display:flex;align-items:center;gap:10px;font-size:14px;letter-spacing:.5px}
.learn i{width:26px;height:26px;border:1px solid #999;border-radius:50%;display:flex;align-items:center;justify-content:center;font-style:normal;font-size:18px;color:#888}
.cause{left:600px;top:1040px;font-size:21px;font-weight:700;color:var(--ink)}
.raised{left:600px;top:1076px;width:521px;font-size:16px;color:var(--ink);display:flex;justify-content:space-between}
.bar{left:600px;top:1108px;width:521px;height:27px;border:1px solid #ccc;background:var(--white)}
.bar div{width:57%;height:100%;background:var(--gold-soft)}
.donate-now{left:600px;top:1158px;width:188px;height:47px}

/* why */
.why{left:0;top:1289px;width:1200px;height:422px;background:var(--grey-bg)}
.sec-title{position:absolute;left:0;width:1200px;text-align:center;font-family:"Crimson Text",Georgia,serif;font-weight:400;font-size:38px;color:var(--ink)}
.sec-rule{position:absolute;left:564px;width:72px;height:3px;background:var(--gold)}
.feature{position:absolute;top:1420px;width:320px;text-align:center}
.feature svg{display:block;margin:0 auto}
.feature h3{font-family:"Crimson Text",Georgia,serif;font-weight:400;font-size:24px;color:var(--ink);margin-top:28px}
.feature p{font-size:14px;line-height:23px;margin-top:8px}

/* split */
.split{top:1718px;height:310px;width:523px;padding:50px 35px}
.split h2{font-family:"Crimson Text",Georgia,serif;font-weight:400;font-size:40px;line-height:40px}
.split p{font-size:14px;line-height:24px;margin-top:16px;width:420px}
.split .btn{position:static;width:163px;height:45px;margin-top:20px}
.split-support{left:77px;background:var(--gold);color:var(--ink)}
.split-support h2{color:var(--ink)}
.split-donate{left:600px;background:var(--dark);color:var(--white)}
.split-donate h2{color:var(--gold)}

/* volunteers */
.vol{position:absolute;top:2162px;width:240px;height:300px;border:1px solid var(--line);background:var(--white)}
.vol.featured{border:2px solid var(--gold)}
.vol-photo{position:absolute;left:0;top:14px;width:100%;height:154px;background:linear-gradient(180deg,#e3e6ea,#c4c9cf)}
.vol-name{position:absolute;top:200px;width:100%;text-align:center;font-family:"Crimson Text",Georgia,serif;font-size:21px;color:var(--ink)}
.vol-rule{position:absolute;left:90px;top:240px;width:60px;height:2px;background:#bbb}
.vol-icons{position:absolute;top:258px;left:0;width:100%;display:flex;justify-content:center;gap:10px}
.vol-icons span{width:28px;height:28px;border:1px solid #bbb}

/* testimonials */
.says{left:0;top:2521px;width:1200px;height:404px;background:var(--grey-bg)}
.quote{position:absolute;top:2672px;width:320px;height:186px;background:var(--dark);text-align:center;padding:60px 22px 0}
.quote p{font-size:14px;line-height:25px;color:var(--white)}
.quote .who{color:var(--gold);font-size:17px;margin-top:14px}
.quote-badge{position:absolute;top:-32px;left:128px;width:64px;height:64px;border-radius:50%;background:var(--gold);display:flex;align-items:center;justify-content:center}

/* news */
.news{position:absolute;top:3044px;width:469px;height:233px;border:1px solid var(--line);background:var(--white)}
.news-photo{position:absolute;top:0;width:209px;height:231px}
.news-date{position:absolute;width:62px;height:74px;background:var(--gold);text-align:center;font-family:"Crimson Text",Georgia,serif;color:var(--ink)}
.news-date b{display:block;font-size:28px;line-height:30px;margin-top:8px}
.news-date small{font-size:13px;letter-spacing:1px}
.news-body{position:absolute;left:228px;top:30px;width:220px}
.news-body h3{font-family:"Crimson Text",Georgia,serif;font-size:22px;line-height:26px;color:var(--ink)}
.news-body p{font-size:14px;line-height:24px;margin-top:10px}

/* footer */
.footer{left:0;top:3352px;width:1200px;height:367px;background:var(--dark);color:#e6e6e6}
.fcol{position:absolute;top:45px;width:320px;font-size:14px;line-height:24px}
.fcol h4{font-family:"Crimson Text",Georgia,serif;font-weight:400;font-size:24px;color:var(--gold);margin-bottom:8px}
.read-more{display:inline-block;margin-top:14px;color:var(--gold);text-decoration:underline;font-family:"Crimson Text",Georgia,serif;font-size:15px;letter-spacing:.5px}
.contact-row{display:flex;gap:16px;align-items:flex-start;margin-bottom:8px}
.contact-row svg{flex:none;margin-top:4px}
.email-field{width:238px;height:38px;background:#f2f2f2;color:#777;font-size:13px;padding:10px 8px;margin-top:12px}
.subscribe{width:146px;height:40px;border:1px solid var(--gold);color:var(--gold);margin-top:12px;display:flex;align-items:center;justify-content:center;font-family:"Crimson Text",Georgia,serif;font-size:17px;letter-spacing:1px}
.f-rule{left:77px;top:302px;width:1046px;height:1px;background:#555}
.copyright{left:0;top:326px;width:1200px;text-align:center;font-size:14px;color:#e6e6e6}
.copyright b{color:var(--gold)}
</style>
</head>
<body>

<header>
  <div class="abs topbar"></div>
  <div class="abs brand"><span class="brand-mark"></span>Lanterns Valley Foundation</div>
  <div class="abs social"><span></span><span></span><span></span><span></span></div>
  <div class="btn btn-gold contact-btn">Contact Us</div>
  <nav class="abs nav">
    <a class="active" style="left:82px">Home</a>
    <a style="left:169px">About</a>
    <a style="left:253px">Donate</a>
    <a style="left:352px">Support Hospitality</a>
    <a style="left:550px">News</a>
    <a style="left:635px">Contact</a>
  </nav>
</header>

<section class="abs hero">
  <div class="abs hero-cloud"></div>
  <h1 class="abs hero-title">financially supporting the<br>treatment of cancer patients</h1>
  <div class="btn btn-gold" style="left:77px;top:293px;width:146px;height:52px">Donate</div>
  <div class="btn btn-gold" style="left:233px;top:293px;width:146px;height:52px">Support</div>
  <div class="abs hero-art" role="img" aria-label="Heart-shaped word cloud of giving words with a large Donate headline on an orange brush stroke"></div>
</section>

<section>
  <div class="abs frame"></div>
  <div class="abs welcome-photo" role="img" aria-label="Woman in a white top forming a heart with her hands around a pink ribbon"></div>
  <h2 class="abs welcome-title">Welcome To Lanterns Valley Foundation</h2>
  <p class="abs welcome-text">Lorem Ipsum is simply dummy text of the printing and typesetting industry. Lorem Ipsum has been the industry's standard dummy text ever since the 1500s, when an unknown printer.</p>
  <div class="abs learn"><i>+</i>LEARN MORE</div>
  <div class="abs cause">Support Cancer Patient For Treatment</div>
  <div class="abs raised"><span>Rised: $1450</span><span>Goal: $2250</span></div>
  <div class="abs bar"><div></div></div>
  <div class="btn btn-dark donate-now">Donate Now</div>
</section>

<section>
  <div class="abs why"></div>
  <h2 class="sec-title" style="top:1328px">Why Choose Us?</h2>
  <div class="sec-rule" style="top:1388px"></div>

  <div class="feature" style="left:88px">
    <svg width="110" height="130" viewBox="0 0 110 130" aria-hidden="true">
      <rect x="10" y="14" width="90" height="110" rx="8" fill="none" stroke="#222" stroke-width="6"/>
      <rect x="36" y="4" width="38" height="20" rx="4" fill="#222"/>
      <path d="M55 86 C35 72 28 62 28 52 C28 42 36 36 44 36 C50 36 53 40 55 44 C57 40 60 36 66 36 C74 36 82 42 82 52 C82 62 75 72 55 86Z" fill="none" stroke="#efc552" stroke-width="4"/>
      <path d="M40 58 L52 68 L74 46" fill="none" stroke="#efc552" stroke-width="4"/>
      <rect x="28" y="98" width="54" height="5" fill="#efc552"/>
    </svg>
    <h3>Better Treatment</h3>
    <p>Lorem Ipsum is simply dummy text of the<br>printing and typesetting industry.</p>
  </div>

  <div class="feature" style="left:445px">
    <svg width="140" height="130" viewBox="0 0 140 130" aria-hidden="true">
      <path d="M8 30 C40 10 80 8 120 24 L100 40 C70 30 45 32 25 42Z" fill="#222"/>
      <path d="M132 100 C100 120 60 122 20 106 L40 90 C70 100 95 98 115 88Z" fill="#222"/>
      <path d="M70 90 C50 76 44 66 44 56 C44 47 51 42 58 42 C64 42 67 46 70 50 C73 46 76 42 82 42 C89 42 96 47 96 56 C96 66 90 76 70 90Z" fill="none" stroke="#efc552" stroke-width="4"/>
    </svg>
    <h3>Bigger Hope</h3>
    <p>Lorem Ipsum is simply dummy text of the<br>printing and typesetting industry.</p>
  </div>

  <div class="feature" style="left:802px">
    <svg width="140" height="130" viewBox="0 0 140 130" aria-hidden="true">
      <path d="M70 122 C30 92 8 70 8 42 C8 20 25 6 44 6 C56 6 65 14 70 24 C75 14 84 6 96 6 C115 6 132 20 132 42 C132 70 110 92 70 122Z" fill="#efc552" stroke="#222" stroke-width="6"/>
    </svg>
    <h3>More Love</h3>
    <p>Lorem Ipsum is simply dummy text of the<br>printing and typesetting industry.</p>
  </div>
</section>

<section>
  <div class="abs split split-support">
    <h2>Support</h2>
    <p>Lorem Ipsum is simply dummy text of the printing and typesetting industry. Lorem Ipsum has been the industry's standard dummy text ever since the 1500s, when an unknown printer.</p>
    <div class="btn btn-dark">Support</div>
  </div>
  <div class="abs split split-donate">
    <h2>Donate</h2>
    <p>Lorem Ipsum is simply dummy text of the printing and typesetting industry. Lorem Ipsum has been the industry's standard dummy text ever since the 1500s, when an unknown printer.</p>
    <div class="btn btn-gold">Donate Now</div>
  </div>
</section>

<section>
  <h2 class="sec-title" style="top:2068px">Our Volunteer</h2>
  <div class="sec-rule" style="top:2126px"></div>

  <div class="vol featured" style="left:77px">
    <div class="vol-photo" role="img" aria-label="Portrait of volunteer in a grey suit"></div>
    <div class="vol-name">Martin O. Hale</div><div class="vol-rule"></div>
    <div class="vol-icons"><span></span><span></span><span></span><span></span></div>
  </div>
  <div class="vol" style="left:345px">
    <div class="vol-photo" role="img" aria-label="Portrait of volunteer in a dark blazer"></div>
    <div class="vol-name">Nadia R. Colvin</div><div class="vol-rule"></div>
    <div class="vol-icons"><span></span><span></span><span></span><span></span></div>
  </div>
  <div class="vol" style="left:612px">
    <div class="vol-photo" role="img" aria-label="Portrait of volunteer in a dark suit"></div>
    <div class="vol-name">Peter Lund</div><div class="vol-rule"></div>
    <div class="vol-icons"><span></span><span></span><span></span><span></span></div>
  </div>
  <div class="vol" style="left:882px">
    <div class="vol-photo" role="img" aria-label="Portrait of volunteer in a dark suit"></div>
    <div class="vol-name">Clara Westby</div><div class="vol-rule"></div>
    <div class="vol-icons"><span></span><span></span><span></span><span></span></div>
  </div>
</section>

<section>
  <div class="abs says"></div>
  <h2 class="sec-title" style="top:2556px">What People Say</h2>
  <div class="sec-rule" style="top:2614px"></div>

  <div class="quote" style="left:77px">
    <div class="quote-badge"><svg width="30" height="24" viewBox="0 0 30 24" aria-hidden="true"><path d="M2 2h11v11c0 5-3 9-8 10l-1-3c3-1 4-3 4-6H2Z M17 2h11v11c0 5-3 9-8 10l-1-3c3-1 4-3 4-6h-6Z" fill="#fff"/></svg></div>
    <p>Lorem Ipsum is simply dummy text of the printing and typesetting industry. Lorem Ipsum has been the industry.</p>
    <p class="who">-Commentetor Name</p>
  </div>
  <div class="quote" style="left:439px">
    <div class="quote-badge"><svg width="30" height="24" viewBox="0 0 30 24" aria-hidden="true"><path d="M2 2h11v11c0 5-3 9-8 10l-1-3c3-1 4-3 4-6H2Z M17 2h11v11c0 5-3 9-8 10l-1-3c3-1 4-3 4-6h-6Z" fill="#fff"/></svg></div>
    <p>Lorem Ipsum is simply dummy text of the printing and typesetting industry. Lorem Ipsum has been the industry.</p>
    <p class="who">-Commentetor Name</p>
  </div>
  <div class="quote" style="left:799px">
    <div class="quote-badge"><svg width="30" height="24" viewBox="0 0 30 24" aria-hidden="true"><path d="M2 2h11v11c0 5-3 9-8 10l-1-3c3-1 4-3 4-6H2Z M17 2h11v11c0 5-3 9-8 10l-1-3c3-1 4-3 4-6h-6Z" fill="#fff"/></svg></div>
    <p>Lorem Ipsum is simply dummy text of the printing and typesetting industry. Lorem Ipsum has been the industry.</p>
    <p class="who">-Commentetor Name</p>
  </div>
</section>

<section>
  <h2 class="sec-title" style="top:2962px">Latest News</h2>
  <div class="sec-rule" style="top:3020px"></div>

  <article class="news" style="left:99px">
    <div class="news-photo" style="left:0;background:linear-gradient(135deg,#5a4a3c,#a88a6c 55%,#e7dccd)" role="img" aria-label="Person reading papers at a desk"></div>
    <div class="news-date" style="left:147px;top:60px"><b>29</b><small>APR</small></div>
    <div class="news-body">
      <h3>Lorem Ipsum is simply dummy text.</h3>
      <p>Lorem Ipsum is simply dummy text of the printing and typesetting industry. Lorem Ipsum has been the industry's standard dummy text.</p>
    </div>
  </article>

  <article class="news" style="left:632px">
    <div class="news-photo" style="left:0;background:linear-gradient(135deg,#f4eee8,#e4c3aa 55%,#c99b7c)" role="img" aria-label="Two hands clasped in support"></div>
    <div class="news-date" style="left:147px;top:128px"><b>29</b><small>APR</small></div>
    <div class="news-body">
      <h3>Lorem Ipsum is simply dummy text.</h3>
      <p>Lorem Ipsum is simply dummy text of the printing and typesetting industry. Lorem Ipsum has been the industry's standard dummy text.</p>
    </div>
  </article>
</section>

<footer class="abs footer">
  <div class="fcol" style="left:82px">
    <h4>About Us</h4>
    <p>Lorem Ipsum is simply dummy text of the printing and typesetting industry. Lorem Ipsum has been the industry's standard dummy text ever since the 1500s, when an unknown printer.</p>
    <span class="read-more">READ MORE</span>
  </div>
  <div class="fcol" style="left:441px">
    <h4>Contact Info</h4>
    <div class="contact-row">
      <svg width="16" height="20" viewBox="0 0 16 20" aria-hidden="true"><path d="M8 0C3.6 0 0 3.4 0 7.6 0 13 8 20 8 20s8-7 8-12.4C16 3.4 12.4 0 8 0Zm0 10.5a3 3 0 1 1 0-6 3 3 0 0 1 0 6Z" fill="#efc552"/></svg>
      <span>Lorem Ipsum is simply dummy text<br>of the printing and typesetting.</span>
    </div>
    <div class="contact-row">
      <svg width="16" height="16" viewBox="0 0 16 16" aria-hidden="true"><path d="M3.5 0.5 6 3.5 4.5 5.5c1 2.2 3.5 4.8 6 6l2-1.5 3 2.5-1.5 3C7 15 1 9 0.5 2Z" fill="#efc552"/></svg>
      <span>123 456 7890</span>
    </div>
    <div class="contact-row">
      <svg width="16" height="14" viewBox="0 0 16 14" aria-hidden="true"><rect x="1" y="1" width="14" height="12" fill="none" stroke="#efc552" stroke-width="1.6"/><path d="M1 2l7 6 7-6" fill="none" stroke="#efc552" stroke-width="1.6"/></svg>
      <span>info@lanternsvalley.org</span>
    </div>
  </div>
  <div class="fcol" style="left:801px">
    <h4>Newsletter</h4>
    <p>Would you like to receive<br>exclusive access to articles, white<br>papers and our regular?</p>
    <div class="email-field">Enter Email Id</div>
    <div class="subscribe">SUBSCRIBE</div>
  </div>
  <div class="abs f-rule"></div>
  <div class="abs copyright">©<b>Lanterns Valley Foundation</b>. 2017 - All Rights Reserved.</div>
</footer>

</body>
</html>
```